KVT Business Cards

We require business cards for our business. We would like a matte black back to the card, with our logo centred in the middle. The front side of the card is open to design.

Target Market(s)

Clients looking for legal services (professional)

Industry/Entity Type

Legal

Contact Information for Business Card

Boris Telemark
Partner
Mobile: 0438 715 642
Email: boris@kvtlaw.co
Website: www.kvtlaw.co
Level 3, 118 Wexbury Street
Sydney NSW 2000

Font styles to use
Other font styles liked:
• Avenir

Colors
f04a50
ffffff
1b1b1b

Requirements
Must have
• Black back with logo included in the centre of the card.
• Our font is Avenir.

```html
<!DOCTYPE html>
<html lang="en">
<head>
<meta charset="utf-8">
<title>KVT Law — Business Cards</title>
<link href="https://fonts.googleapis.com/css2?family=Mulish:wght@400;600;800&display=swap" rel="stylesheet">
<style>
  :root {
    --stage: #2b2b2b;
    --card: #1b1b1b;
    --card-light: #262626;
    --crimson: #d01f48;
    --white: #ffffff;
    --soft: #d9d9d9;
    --rule: #6a6a6a;
  }
  * { box-sizing: border-box; margin: 0; padding: 0; }
  html, body {
    width: 1200px;
    height: 960px;
    overflow: hidden;
    background: var(--stage);
    font-family: "Mulish", "Avenir", sans-serif;
  }
  .canvas {
    position: relative;
    width: 1200px;
    height: 960px;
  }
  .card {
    position: absolute;
    left: 250px;
    width: 700px;
    height: 400px;
    background: radial-gradient(ellipse at 40% 35%, var(--card-light) 0%, var(--card) 70%);
    box-shadow: 0 18px 40px rgba(0,0,0,.45);
  }
  .card--back { top: 60px; }
  .card--front { top: 500px; }

  /* Brand lockup: plain square + firm name */
  .brand {
    display: flex;
    align-items: center;
    gap: 18px;
  }
  .brand__square {
    background: var(--crimson);
  }
  .brand__name {
    color: var(--white);
    font-weight: 800;
    letter-spacing: .04em;
    text-transform: uppercase;
    line-height: 1;
  }

  /* Back */
  .card--back .brand {
    position: absolute;
    left: 50%;
    top: 150px;
    transform: translateX(-50%);
    gap: 24px;
  }
  .card--back .brand__square { width: 62px; height: 62px; }
  .card--back .brand__name { font-size: 54px; }
  .back__web {
    position: absolute;
    left: 0; right: 0;
    top: 290px;
    text-align: center;
    font-size: 17px;
    font-weight: 600;
    letter-spacing: .32em;
    color: var(--soft);
  }
  .back__web .accent { color: var(--crimson); }

  /* Front */
  .card--front .brand {
    position: absolute;
    left: 48px;
    top: 112px;
  }
  .card--front .brand__square { width: 40px; height: 40px; }
  .card--front .brand__name { font-size: 34px; }
  .front__rule {
    position: absolute;
    left: 340px;
    top: 70px;
    width: 1px;
    height: 260px;
    background: var(--rule);
  }
  .contact {
    position: absolute;
    left: 372px;
    top: 82px;
    color: var(--soft);
  }
  .contact__name {
    color: var(--crimson);
    font-weight: 800;
    font-size: 23px;
    letter-spacing: .03em;
    text-transform: uppercase;
    line-height: 1.1;
  }
  .contact__role {
    font-size: 15px;
    letter-spacing: .08em;
    text-transform: uppercase;
    margin-bottom: 18px;
  }
  .contact__address {
    font-size: 16px;
    line-height: 1.45;
    margin-bottom: 18px;
  }
  .contact__list { list-style: none; }
  .contact__item {
    display: flex;
    align-items: center;
    gap: 12px;
    font-size: 16px;
    line-height: 1.9;
  }
  .contact__icon {
    width: 17px;
    height: 17px;
    flex: none;
  }
</style>
</head>
<body>
<main class="canvas">

  <section class="card card--back" aria-label="Card back">
    <div class="brand">
      <span class="brand__square"></span>
      <span class="brand__name">KVT Law</span>
    </div>
    <p class="back__web">www.<span class="accent">kvtlaw</span>.co</p>
  </section>

  <section class="card card--front" aria-label="Card front">
    <div class="brand">
      <span class="brand__square"></span>
      <span class="brand__name">KVT Law</span>
    </div>
    <span class="front__rule"></span>
    <div class="contact">
      <h1 class="contact__name">Boris Telemark</h1>
      <p class="contact__role">Partner</p>
      <p class="contact__address">Level 3, 118 Wexbury Street<br>Sydney NSW 2000</p>
      <ul class="contact__list">
        <li class="contact__item">
          <svg class="contact__icon" viewBox="0 0 24 24" fill="none" stroke="#d01f48" stroke-width="2"><rect x="6" y="2" width="12" height="20" rx="2"/><line x1="10" y1="18" x2="14" y2="18"/></svg>
          0438 715 642
        </li>
        <li class="contact__item">
          <svg class="contact__icon" viewBox="0 0 24 24" fill="#d01f48"><path d="M2 5h20v14H2z"/><path d="M2 5l10 8 10-8" fill="none" stroke="#1b1b1b" stroke-width="1.8"/></svg>
          boris@kvtlaw.co
        </li>
        <li class="contact__item">
          <svg class="contact__icon" viewBox="0 0 24 24" fill="none" stroke="#d01f48" stroke-width="2"><circle cx="12" cy="12" r="10"/><ellipse cx="12" cy="12" rx="4.5" ry="10"/><line x1="2" y1="12" x2="22" y2="12"/></svg>
          www.kvtlaw.co
        </li>
      </ul>
    </div>
  </section>

</main>
</body>
</html>
```